11 x 17 Orvanthes Quote

Design the following quote in a poster.

"First say to yourself what you would be; then do what you have to do." - Orvanthes

See here for inspiration - https://prints.mornbrekal.com/

Quote

```html
<!DOCTYPE html>
<html lang="en">
<head>
<meta charset="utf-8">
<title>Orvanthes Quote Poster</title>
<link rel="stylesheet" href="https://fonts.googleapis.com/css2?family=Gelasio:wght@700&display=swap">
<style>
  :root {
    --frame: #e6e6e6;
    --tone-top: #a8a8a8;
    --tone-mid: #6a6a6a;
    --tone-bottom: #262626;
    --ink: #ffffff;
    --glow: rgba(60, 60, 60, 0.75);
  }
  * { margin: 0; padding: 0; box-sizing: border-box; }
  html, body {
    width: 960px;
    height: 1200px;
    overflow: hidden;
    background: var(--frame);
  }
  .poster {
    position: relative;
    width: 960px;
    height: 1200px;
    background: var(--frame);
  }
  .photo-area {
    position: absolute;
    left: 12px;
    top: 12px;
    width: 936px;
    height: 1176px;
    background: linear-gradient(to bottom, var(--tone-top) 0%, var(--tone-mid) 50%, var(--tone-bottom) 100%);
  }
  .quote {
    position: absolute;
    left: 0;
    top: 80px;
    width: 960px;
    text-align: center;
    font-family: "Gelasio", Georgia, serif;
    font-weight: 700;
    font-size: 92px;
    line-height: 139px;
    color: var(--ink);
    text-shadow: 0 0 14px var(--glow), 0 2px 6px var(--glow);
    letter-spacing: -0.5px;
  }
  .quote .line { display: block; white-space: nowrap; }
  .rule {
    position: absolute;
    left: 290px;
    top: 812px;
    width: 370px;
    height: 2px;
    background: var(--ink);
    box-shadow: 0 0 6px var(--glow);
  }
  .attribution {
    position: absolute;
    left: 0;
    top: 848px;
    width: 960px;
    text-align: center;
    font-family: "Gelasio", Georgia, serif;
    font-weight: 700;
    font-size: 27px;
    letter-spacing: 6px;
    color: var(--ink);
    text-shadow: 0 0 6px var(--glow);
  }
</style>
</head>
<body>
  <main class="poster">
    <div class="photo-area" role="img" aria-label="Black and white photograph of the ocean at sunset with rocks in the foreground"></div>

    <h1 class="quote">
      <span class="line">"First say to</span>
      <span class="line">yourself what</span>
      <span class="line">you would be;</span>
      <span class="line">then do what</span>
      <span class="line">you have to do."</span>
    </h1>
    <div class="rule"></div>
    <p class="attribution">Orvanthes</p>
  </main>
</body>
</html>
```